Freeze dried pet treats and chews packaging design

We are an Belgium based brand selling all natural treats and chews for pets. We are looking for a full color packaging design for a new line of freeze dried treats and chews for cats and dogs. The design should look familiar for our customers with our existing logo, but with a fresh new design especially for this new line. It should reflect our core values of natural, species appropriate food products without any additives or nasties.
The packaging will be a stand-up pouch with zipper, eurohole, easy open and with a window somewhere in the design to show the products inside. Please present your design as a mockup if possible.
Name of the product will be "Velmo Freeze Dried Bitzoos". Add icons to emphasize certain aspects of the product:
- 100% natural
- freeze dried (preserves all nutrients best)
- 100% mono protein
- without additives
- high in protein
- high in flavor
The design is a generic one for 12 different products, only one pouch will be produced and finished with 12 different round labels to indicate the protein source (beef, chicken, lamb, etc). You can include one of these stickers on your design to make the example complete. The sticker should have a separate color for every protein source to make it good distinguishable, an icon representing the protein source (see examples of existing packaging) and a round text around it with the protein source in text in Dutch, French and English (example: RUND - BŒUF - BEEF).
Important: after this design we need more designs for other new product lines, so the winner might get more out of this then only this one project!
High premium pet products
Petfood
- Fontastique, Roboto (used for logo and current designs), others welcome too

```html
<!DOCTYPE html>
<html lang="en">
<head>
<meta charset="utf-8">
<title>Velmo Freeze Dried Bitzoos – Pouch</title>
<link href="https://fonts.googleapis.com/css2?family=Fredoka:wght@500;600;700&display=swap" rel="stylesheet">
<style>
  :root{
    --stage:#c9c8ec;
    --pouch-white:#fbfcf4;
    --lime:#c8e63a;
    --lime-deep:#8cc21c;
    --purple:#7a33c8;
    --purple-deep:#5a1fa6;
    --night:#2c1650;
    --product:#9c7f63;
    --product-dark:#6f5640;
    --white:#ffffff;
  }
  html,body{margin:0;padding:0;}
  body{
    width:1200px;height:607px;overflow:hidden;
    background:var(--stage);
    display:flex;align-items:center;justify-content:center;
  }
  .pouch{width:406px;height:560px;display:block;filter:drop-shadow(0 8px 14px rgba(40,20,90,.25));}
  .brand-name{font-family:"Fredoka",sans-serif;font-weight:600;fill:var(--purple-deep);}
  .title{font-family:"Fredoka",sans-serif;font-weight:700;fill:var(--purple);stroke:var(--white);stroke-width:3;paint-order:stroke;}
  .icon-caption{font-family:"Fredoka",sans-serif;font-weight:600;font-size:8.5px;letter-spacing:.3px;fill:var(--white);}
  .protein-label{font-family:"Fredoka",sans-serif;font-weight:500;font-size:26px;letter-spacing:3px;fill:var(--white);}
</style>
</head>
<body>
<svg class="pouch" viewBox="0 0 580 800" xmlns="http://www.w3.org/2000/svg" aria-label="Velmo Freeze Dried Bitzoos pouch">
  <defs>
    <linearGradient id="pouch-bg" x1="0" y1="0" x2="0" y2="1">
      <stop offset="0" stop-color="var(--pouch-white)"/>
      <stop offset=".35" stop-color="#eef6c8"/>
      <stop offset=".7" stop-color="var(--lime)"/>
      <stop offset="1" stop-color="var(--lime-deep)"/>
    </linearGradient>
    <radialGradient id="product-fill" cx=".45" cy=".45" r=".6">
      <stop offset="0" stop-color="var(--product)"/>
      <stop offset="1" stop-color="var(--product-dark)"/>
    </radialGradient>
    <clipPath id="pouch-shape"><rect x="0" y="0" width="580" height="800" rx="16"/></clipPath>
    <path id="label-arc" d="M180 640 A190 150 0 0 0 540 640"/>
    <path id="cap-arc" d="M-25 2 A25 25 0 0 1 25 2"/>
  </defs>

  <g clip-path="url(#pouch-shape)">
    <rect class="pouch-body" width="580" height="800" fill="url(#pouch-bg)"/>
    <path d="M0 520 C120 430 220 360 420 330 C500 318 560 330 580 340 L580 800 L0 800Z" fill="var(--lime)" opacity=".55"/>
    <path d="M0 640 C80 560 150 520 230 500 L580 560 L580 800 L0 800Z" fill="var(--purple)"/>
    <path d="M0 720 C120 660 260 650 420 700 C500 725 560 730 580 725 L580 800 L0 800Z" fill="var(--night)"/>
    <!-- window frame -->
    <circle cx="375" cy="540" r="170" fill="var(--purple)"/>
    <circle class="product-window" cx="372" cy="548" r="138" fill="url(#product-fill)" stroke="var(--white)" stroke-width="4" role="img" aria-label="Window showing freeze dried beef chunks inside a cow head outline"/>
    <!-- protein label band -->
    <path d="M180 640 A190 150 0 0 0 540 640" fill="none" stroke="var(--white)" stroke-width="50" stroke-linecap="round"/>
    <path d="M180 640 A190 150 0 0 0 540 640" fill="none" stroke="var(--night)" stroke-width="42" stroke-linecap="round"/>
    <text class="protein-label"><textPath href="#label-arc" startOffset="50%" text-anchor="middle" dy="9">RUND - BŒUF - BEEF</textPath></text>
  </g>

  <!-- euro hole -->
  <rect x="228" y="26" width="124" height="24" rx="12" fill="#eef0f6" stroke="#d3d5e2"/>
  <!-- origin tab -->
  <rect x="435" y="0" width="95" height="115" fill="var(--lime-deep)"/>
  <circle cx="482" cy="72" r="40" fill="var(--white)"/>
  <circle cx="482" cy="72" r="32" fill="var(--purple)"/>

  <!-- brand -->
  <circle cx="62" cy="200" r="9" fill="var(--lime-deep)"/>
  <text class="brand-name" x="80" y="222" font-size="64">Velmo</text>

  <!-- product title -->
  <text class="title" x="285" y="215" font-size="72" textLength="240" lengthAdjust="spacingAndGlyphs">FREEZE</text>
  <text class="title" x="283" y="305" font-size="92" textLength="242" lengthAdjust="spacingAndGlyphs">DRIED</text>
  <text class="title" x="282" y="360" font-size="56" textLength="244" lengthAdjust="spacingAndGlyphs">BITZOOS</text>

  <!-- benefit icons -->
  <g class="benefit" transform="translate(112 330)">
    <circle r="36" fill="var(--purple-deep)" stroke="var(--white)" stroke-width="2"/>
    <text class="icon-caption" text-anchor="middle"><textPath href="#cap-arc" startOffset="50%">100% NATURAL</textPath></text>
    <path transform="translate(0 6) scale(.8)" d="M0 16 V2 M0 6 C-4 -6 -14 -6 -16 0 C-10 6 -4 6 0 6 M0 4 C4 -8 14 -8 16 -2 C10 4 4 4 0 4" fill="none" stroke="var(--lime)" stroke-width="2.5"/>
  </g>
  <g class="benefit" transform="translate(112 410)">
    <circle r="36" fill="var(--purple-deep)" stroke="var(--white)" stroke-width="2"/>
    <text class="icon-caption" text-anchor="middle"><textPath href="#cap-arc" startOffset="50%">FREEZE DRIED</textPath></text>
    <path transform="translate(0 4) scale(.8)" d="M0 -12 V16 M-13 -5 L13 9 M-13 9 L13 -5" fill="none" stroke="var(--lime)" stroke-width="2.5" stroke-linecap="round"/>
  </g>
  <g class="benefit" transform="translate(112 490)">
    <circle r="36" fill="var(--purple-deep)" stroke="var(--white)" stroke-width="2"/>
    <text class="icon-caption" text-anchor="middle"><textPath href="#cap-arc" startOffset="50%">MONO PROTEIN</textPath></text>
    <path transform="translate(0 8) scale(.8)" d="M-14 2 C-10 -10 -6 14 -2 2 C2 -10 6 14 10 2 C12 -4 14 -4 15 0" fill="none" stroke="var(--lime)" stroke-width="3"/>
  </g>
  <g class="benefit" transform="translate(112 570)">
    <circle r="36" fill="var(--purple-deep)" stroke="var(--white)" stroke-width="2"/>
    <text class="icon-caption" text-anchor="middle"><textPath href="#cap-arc" startOffset="50%">NO ADDITIVES</textPath></text>
    <path transform="translate(0 8) scale(.75)" d="M-4 -10 V0 L-11 14 H11 L4 0 V-10 M-16 -12 L16 16" fill="none" stroke="var(--lime)" stroke-width="2.5"/>
  </g>
  <g class="benefit" transform="translate(112 650)">
    <circle r="36" fill="var(--lime-deep)" stroke="var(--white)" stroke-width="2"/>
    <text class="icon-caption" text-anchor="middle"><textPath href="#cap-arc" startOffset="50%">HIGH PROTEIN</textPath></text>
    <path transform="translate(0 7) scale(.8)" d="M0 -12 L13 2 H5 V15 H-5 V2 H-13Z" fill="none" stroke="var(--white)" stroke-width="2.5" stroke-linejoin="round"/>
  </g>
  <g class="benefit" transform="translate(112 730)">
    <circle r="36" fill="var(--lime-deep)" stroke="var(--white)" stroke-width="2"/>
    <text class="icon-caption" text-anchor="middle"><textPath href="#cap-arc" startOffset="50%">HIGH FLAVOR</textPath></text>
    <g transform="translate(0 6) scale(.8)">
      <circle cy="3" r="14" fill="none" stroke="var(--white)" stroke-width="2.5"/>
      <path d="M-7 6 C-3 12 3 12 7 6" fill="none" stroke="var(--white)" stroke-width="2.5"/>
    </g>
  </g>
</svg>
</body>
</html>
```